Need Business Card for eLearning Company

Need a business card designed for our company, CareerPathlane.

CareerPathlane has developed a complete 12 lesson eLearning course to teach you the skills you need to present yourself in a job interview. The course uses advanced learning techniques in the multimedia videos, plus contains quizzes and additional exercises to insure you get the course and can walk into any interview with confidence and ease, and get the job.

www.careerpathlane-demo.com

Attached is our logo

Industry/Entity Type

Business

```html
<!DOCTYPE html>
<html lang="en">
<head>
<meta charset="utf-8">
<title>CareerPathlane Business Card</title>
<link href="https://fonts.googleapis.com/css2?family=Didact+Gothic&display=swap" rel="stylesheet">
<style>
  :root {
    --canvas-bg: #e4e2df;
    --brand-purple: #7b1a6c;
    --brand-green: #8cb33a;
    --card-white: #f3f3f3;
    --ink-dark: #3c3c3c;
    --ink-soft: #555555;
    --mark-grey: #4a4a4a;
    --on-purple: #ffffff;
  }
  * { box-sizing: border-box; margin: 0; padding: 0; }
  html, body {
    width: 1200px;
    height: 900px;
    overflow: hidden;
  }
  body {
    background: var(--canvas-bg);
    font-family: "Didact Gothic", "Century Gothic", sans-serif;
    position: relative;
  }
  .card {
    position: absolute;
    width: 525px;
    height: 300px;
    border-radius: 3px;
    box-shadow: 0 10px 24px rgba(0,0,0,0.18);
  }

  /* Front side */
  .card-front {
    left: 70px;
    top: 140px;
    background: var(--brand-purple);
    color: var(--on-purple);
    display: flex;
    flex-direction: column;
    align-items: center;
    justify-content: center;
  }
  .front-square {
    width: 58px;
    height: 58px;
    background: var(--on-purple);
    border-radius: 8px;
    margin-bottom: 24px;
  }
  .front-name {
    font-size: 40px;
    letter-spacing: 0.5px;
    line-height: 1;
  }

  /* Back side */
  .card-back {
    left: 605px;
    top: 460px;
    background: var(--card-white);
    color: var(--ink-dark);
    padding: 44px 40px 0 40px;
  }
  .back-header {
    display: flex;
    align-items: center;
    gap: 16px;
  }
  .back-square {
    width: 44px;
    height: 44px;
    background: var(--mark-grey);
    border-radius: 6px;
    flex: none;
  }
  .back-name {
    font-size: 34px;
    line-height: 1;
    color: var(--ink-dark);
  }
  .person {
    margin-top: 40px;
    display: flex;
    align-items: baseline;
    gap: 12px;
  }
  .person-name {
    font-size: 24px;
  }
  .person-title {
    font-size: 14px;
    letter-spacing: 0.8px;
    text-transform: uppercase;
  }
  .contact-list {
    margin-top: 20px;
    list-style: none;
    font-size: 13px;
    line-height: 1.75;
    color: var(--ink-soft);
    white-space: nowrap;
  }
  .contact-label {
    color: var(--brand-green);
    margin-right: 3px;
  }
  .contact-sep {
    margin: 0 5px;
  }
</style>
</head>
<body>

  <section class="card card-front" aria-label="Business card front">
    <div class="front-square" aria-hidden="true"></div>
    <div class="front-name">CareerPathlane</div>
  </section>

  <section class="card card-back" aria-label="Business card back">
    <header class="back-header">
      <div class="back-square" aria-hidden="true"></div>
      <div class="back-name">CareerPathlane</div>
    </header>

    <div class="person">
      <span class="person-name">Dana Whitford</span>
      <span class="person-title">Principal Consultant</span>
    </div>

    <ul class="contact-list">
      <li><span class="contact-label">T</span>(555) 014-2290<span class="contact-sep">|</span><span class="contact-label">E</span>support@careerpathlane-demo.com</li>
      <li>2240 Harbor Crest Road Suite 310, Fairview, WA 98000</li>
      <li>www.careerpathlane-demo.com</li>
    </ul>
  </section>

</body>
</html>
```